Telecommunications/Power civil contractor needs business card design

Were a new telecommunications/power underground civil contractor that is looking for a new business card design. Our company colours are silver or grey and orange. Feel free to use the white background logo or the black background logo.

Target Market(s)

Local contractors, utility companies, private sector mining/energy companies, developers.

Industry/Entity Type

Telecommunications

Contact Information for Business Card

Each card will need the following info:
Persons name:
Title:
E-mail:
Phone number:
Shop Address:
Mailing Address:

Requirements
Must have
• Each card will need the following info:
• Persons name:
• Title:
• E-mail:
• Phone number:
• Shop Address:
• Mailing Address:

```html
<!DOCTYPE html>
<html lang="en">
<head>
<meta charset="utf-8">
<title>Korven Civil Works – Business Card</title>
<link href="https://fonts.googleapis.com/css2?family=Montserrat:wght@400;500;700;800&display=swap" rel="stylesheet">
<style>
  :root {
    --orange: #f0582a;
    --grey: #6b6b6b;
    --grey-light: #a9a9a9;
    --grey-dark: #4a4a4a;
    --black: #050505;
    --white: #ffffff;
    --stage: #2b2b2b;
  }
  html, body {
    margin: 0;
    padding: 0;
    width: 1200px;
    height: 900px;
    overflow: hidden;
    background: var(--stage);
    font-family: "Montserrat", sans-serif;
  }
  .canvas { position: relative; width: 1200px; height: 900px; }
  .card {
    position: absolute;
    width: 640px;
    height: 366px;
    border-radius: 22px;
    overflow: hidden;
    box-shadow: 0 10px 30px rgba(0,0,0,.45);
  }

  /* Back of card */
  .card-back { left: 80px; top: 70px; background: var(--black); }
  .card-back .brand-row {
    position: absolute; left: 120px; top: 120px;
    display: flex; align-items: center; gap: 26px;
  }
  .brand-dot {
    width: 120px; height: 120px; border-radius: 50%;
    border: 6px solid var(--grey-light); box-sizing: border-box;
  }
  .card-back .brand-name {
    color: var(--orange); font-weight: 800; font-size: 30px;
    line-height: 1.05; letter-spacing: 1px; margin: 0;
  }
  .card-back .website {
    position: absolute; left: 0; right: 0; bottom: 46px;
    text-align: center; color: var(--white); font-size: 17px; letter-spacing: .5px;
  }
  .card-back .website b { font-weight: 700; }

  /* Front of card */
  .card-front { left: 480px; top: 464px; background: var(--white); }
  .card-front .art { position: absolute; inset: 0; }
  .card-front .brand-name {
    position: absolute; left: 34px; top: 62px; margin: 0;
    color: var(--orange); font-weight: 800; font-size: 27px;
    line-height: 1.05; letter-spacing: 1px;
  }
  .person { position: absolute; left: 40px; top: 152px; }
  .person-name { color: var(--orange); font-size: 24px; font-weight: 500; margin: 0; letter-spacing: .5px; }
  .person-title { color: var(--grey); font-size: 15px; margin: 2px 0 14px; }
  .address { color: var(--grey); font-size: 16px; line-height: 1.25; margin: 0 0 4px; }
  .contact {
    position: absolute; right: 24px; top: 196px;
    text-align: right; color: var(--white); font-size: 13px; line-height: 1.5;
    white-space: nowrap;
  }
  .contact p { margin: 0; display: flex; justify-content: flex-end; align-items: center; gap: 7px; }
  .contact svg { width: 12px; height: 12px; }
</style>
</head>
<body>
<div class="canvas">

  <section class="card card-back">
    <div class="brand-row">
      <div class="brand-dot"></div>
      <p class="brand-name">KORVEN CIVIL<br>WORKS INC</p>
    </div>
    <p class="website">www.<b>korvencivil</b>.com</p>
  </section>

  <section class="card card-front">
    <svg class="art" viewBox="0 0 640 366" aria-hidden="true">
      <defs>
        <linearGradient id="panel" x1="0" y1="0" x2="1" y2="1">
          <stop offset="0" stop-color="#8a8a8a"/>
          <stop offset=".5" stop-color="#b4b4b4"/>
          <stop offset="1" stop-color="#5e5e5e"/>
        </linearGradient>
      </defs>
      <path d="M450 0 L640 0 L640 366 L160 366 C300 330 360 290 372 190 C384 90 410 30 450 0 Z" fill="url(#panel)"/>
      <path d="M440 0 C400 30 374 90 362 190 C350 290 290 330 150 366" fill="none" stroke="var(--orange)" stroke-width="5"/>
      <path d="M0 338 C90 350 150 352 220 340 L240 366 L0 366 Z" fill="#7a7a7a"/>
      <path d="M0 352 C80 360 150 362 200 356 L206 366 L0 366 Z" fill="var(--orange)"/>
      <rect x="560" y="42" width="80" height="12" fill="var(--orange)"/>
      <circle cx="510" cy="90" r="68" fill="var(--white)" stroke="var(--grey-dark)" stroke-width="5"/>
    </svg>

    <p class="brand-name">KORVEN CIVIL<br>WORKS INC</p>

    <div class="person">
      <p class="person-name">MAREK HOLLOWAY</p>
      <p class="person-title">Director</p>
      <p class="address">48 Foundry Lane<br>Millbrook, NY 12545</p>
      <p class="address">PO BOX 3150<br>LAKEVIEW, CA 91302</p>
    </div>

    <div class="contact">
      <p>+330 5182-4406
        <svg viewBox="0 0 24 24"><path d="M6.6 10.8a15 15 0 006.6 6.6l2.2-2.2a1 1 0 011-.25 11.4 11.4 0 003.6.57 1 1 0 011 1V20a1 1 0 01-1 1A17 17 0 013 4a1 1 0 011-1h3.5a1 1 0 011 1c0 1.250.2 2.450.57 3.57a1 1 0 01-.25 1z" fill="var(--orange)"/></svg>
      </p>
      <p>info@korvencivil.com
        <svg viewBox="0 0 24 24"><rect x="2" y="5" width="20" height="14" rx="2" fill="none" stroke="var(--orange)" stroke-width="2"/><path d="M3 6l9 7 9-7" fill="none" stroke="var(--orange)" stroke-width="2"/></svg>
      </p>
      <p>77 yard street, 77 mailing address</p>
      <p>Fraser bc Canada, V3k 2p8</p>
    </div>
  </section>

</div>
</body>
</html>
```